依頼詳細
デザイン住宅の看板デザインをお願いします。
生活道路沿いの路上看板のデザインになります。
事務所上の看板デザインに沿って頂き、シンプルで目立つ看板のデザインでお願いします。
記載項目
会社名:株式会社キリノハコビヤ
電話番号:0574-83-5167
ロゴ(添付ファイル)
看板写真(添付ファイル:宮鶴屋さんの下部分になります)
参考:事務所上の看板(添付ファイル)
希望イメージ
希望する色
水色系、無彩色系
納品ファイル
• 高解像度JPG (.jpg)
• イラストレーター形式 (.ai)
• フォトショップ形式 (.psd)
• PNG形式 (.png)
補足説明
〇想い
高性能でカッコいい家をどこよりもお値打ちに
家づくりは楽しくなくてはならない
家族みんなが毎日笑顔になるオリジナルの家
想いをカタチにできる家
地震に強く、高性能は当たり前

〇メインターゲット
子育て世代・共働き世代
大手ハウスメーカー層から降りてこられるお客様
デザイン住宅(設計事務所)から降りてこられるお客様
看板サイズ 幅1350mm×高さ2500mm

看板の位置の写真の追加させて頂きます。
■ 選んだ理由

シンプルさの中に、親しみを一番感じました。
優しいコントラストの中に、温かみも含まれてると感じ、
こちらのご提案を採用させて頂きました。

■ 提案者全員のお礼・コメント

たくさんのご提案を頂き、ありがとうございました!
正直こんなにご提案頂けるとは思っておらず、
皆さまのデザインに対する想いがすごく伝わり、とても勉強になりました。
次の機会があれば、またご依頼させて頂きたいと思います。
ありがとうございました!

```html
<!DOCTYPE html>
<html lang="ja">
<head>
<meta charset="utf-8">
<title>株式会社キリノハコビヤ 看板デザイン</title>
<link rel="stylesheet" href="https://fonts.googleapis.com/css2?family=Cinzel:wght@400&family=Noto+Sans+JP:wght@400;700;900&display=swap">
<style>
  :root {
    --page: #ffffff;
    --frame-line: #c9c9c9;
    --panel: #ffffff;
    --wood-light: #efe2c8;
    --wood-mid: #e2cfac;
    --wood-dark: #d6c09a;
    --ink: #111111;
    --rule: #ffffff;
    --caption: #333333;
  }
  html, body {
    margin: 0;
    padding: 0;
    width: 846px;
    height: 1200px;
    overflow: hidden;
    background: var(--page);
  }
  .canvas {
    position: relative;
    width: 846px;
    height: 1200px;
    background: var(--page);
    font-family: "Noto Sans JP", sans-serif;
  }
  .sign-stand {
    position: absolute;
    left: 147px;
    top: 23px;
    width: 556px;
    height: 1085px;
    border: 2px solid var(--frame-line);
    box-sizing: border-box;
    background: var(--panel);
  }
  .sign-board {
    position: absolute;
    left: 160px;
    top: 40px;
    width: 530px;
    height: 1032px;
    background: var(--panel);
    overflow: hidden;
  }
  .wood-panel {
    position: absolute;
    left: 136px;
    top: 0;
    width: 394px;
    height: 100%;
    background:
      repeating-linear-gradient(90deg, rgba(190,160,115,0.18) 0 2px, transparent 2px 9px),
      linear-gradient(90deg, var(--wood-mid), var(--wood-light) 45%, var(--wood-dark));
  }
  .inner-rule {
    position: absolute;
    left: 80px;
    top: 45px;
    width: 423px;
    height: 945px;
    border: 3px solid var(--rule);
    box-sizing: border-box;
  }
  .brand-vertical {
    position: absolute;
    left: 37px;
    top: 45px;
    width: 945px;
    height: 0;
    transform-origin: 0 0;
    transform: translateX(42px) rotate(90deg);
    font-family: "Cinzel", serif;
    font-size: 50px;
    letter-spacing: 5px;
    color: var(--ink);
    white-space: nowrap;
    line-height: 1;
    text-align: center;
  }
  .company {
    position: absolute;
    left: 165px;
    top: 340px;
    color: var(--ink);
  }
  .company-prefix {
    display: block;
    font-weight: 700;
    font-size: 40px;
    line-height: 1.2;
    margin-bottom: 6px;
  }
  .company-name {
    display: block;
    font-weight: 900;
    font-size: 74px;
    line-height: 1.15;
    letter-spacing: 2px;
  }
  .phone {
    position: absolute;
    left: 165px;
    top: 922px;
    display: flex;
    align-items: center;
    gap: 12px;
    font-weight: 700;
    font-size: 38px;
    color: var(--ink);
    letter-spacing: 1px;
  }
  .phone svg { width: 30px; height: 30px; }
  .caption {
    position: absolute;
    left: 0;
    top: 1156px;
    width: 100%;
    text-align: center;
    font-size: 19px;
    color: var(--caption);
  }
</style>
</head>
<body>
<div class="canvas">
  <div class="sign-stand"></div>
  <div class="sign-board">
    <div class="wood-panel" role="img" aria-label="明るい木目調のパネル"></div>
    <div class="inner-rule"></div>
    <div class="brand-vertical">KIRINO HAKOBIYA</div>
    <h1 class="company" style="margin:0">
      <span class="company-prefix">株式会社</span>
      <span class="company-name">キリノ</span>
      <span class="company-name">ハコビヤ</span>
    </h1>
    <p class="phone" style="margin:0">
      <svg viewBox="0 0 24 24" aria-hidden="true"><path fill="#111" d="M6.6 10.8a15.1 15.1 0 0 0 6.6 6.6l2.2-2.2a1 1 0 0 1 1-.25 11.4 11.4 0 0 0 3.6.57 1 1 0 0 1 1 1V20a1 1 0 0 1-1 1A17 17 0 0 1 3 4a1 1 0 0 1 1-1h3.5a1 1 0 0 1 1 1c0 1.25.2 2.45.57 3.57a1 1 0 0 1-.25 1z"/></svg>
      0574-83-5167
    </p>
  </div>
  <p class="caption" style="margin:0">株式会社キリノハコビヤ様　看板デザインF案</p>
</div>
</body>
</html>
```